Tabloid Magazine Flyer Class Action Lawsuit

Create a bold, 2-page 8.5" x 11" flyer with the look and feel of a tabloid exposé — loud, sensational, and impossible to ignore. Use bold fonts, dramatic headlines, and high-contrast colors (red, black, white, deep blue). Fill every inch of space — no white space, no subtlety. Use the provided images prominently. Page 1 should grab attention with a shocking headline, impactful image, and strong call to action. Page 2 should stack bold subheadings and explosive bullet points. Emphasize urgency, outrage, and grassroots power. This flyer is meant to rally a community.
Updates

Need to extend because we haven't received a design that meets our needs

Target Market(s)

All instructions and content are in the attached word doc

Industry/Entity Type

Requirements
Must have
• All instructions and content are in the attached word doc
Nice to have
Should not have

```html
<!DOCTYPE html>
<html lang="en">
<head>
<meta charset="utf-8">
<title>Harbor Point Park Exposed – Two-Page Flyer</title>
<link rel="stylesheet" href="https://fonts.googleapis.com/css2?family=Anton&family=Oswald:wght@500;700&family=Montserrat:wght@500;700;800&display=swap">
<style>
  :root{
    --red:#d92b2b;
    --red-deep:#b51f22;
    --blue:#1f3f8f;
    --navy:#14254f;
    --white:#ffffff;
    --ink:#1b1b1b;
    --yellow:#ffd23a;
    --canvas:#ffffff;
  }
  *{box-sizing:border-box;margin:0;padding:0}
  html,body{width:1200px;height:1200px;overflow:hidden;background:var(--canvas)}
  body{position:relative;font-family:"Montserrat",Arial,sans-serif;color:var(--blue)}
  .page{position:absolute;top:250px;width:540px;height:699px;background:var(--white);overflow:hidden;box-shadow:0 6px 18px rgba(0,0,0,.18)}
  .page--front{left:30px}
  .page--back{left:630px}
  .abs{position:absolute}
  .shapes{position:absolute;inset:0;width:100%;height:100%}

  /* FRONT */
  .brand{left:20px;top:26px;display:flex;align-items:center;gap:8px;font-family:"Oswald",sans-serif;font-weight:700;font-size:19px;line-height:1;color:var(--red);letter-spacing:.5px}
  .brand__dot{width:22px;height:22px;border-radius:50%;background:var(--blue);flex:none}
  .hero-photo{left:0;top:90px;width:300px;height:240px;background:linear-gradient(160deg,#c65a4e 0%,#8c2e2b 55%,#4b1b1f 100%)}
  .headline{left:292px;top:58px;width:232px;font-family:"Anton",sans-serif;font-size:66px;line-height:1.02;color:var(--white);text-transform:uppercase}
  .alert-banner{left:0;top:205px;width:290px;padding:12px 18px 12px 20px;font-family:"Oswald",sans-serif;font-weight:700;font-size:19px;line-height:1.15;color:var(--white);text-transform:uppercase}
  .rally{left:20px;top:352px;width:250px}
  .rally__invite{font-family:"Oswald",sans-serif;font-weight:700;font-size:26px;line-height:1.1;color:var(--blue)}
  .rally__event{margin-top:6px;font-family:"Oswald",sans-serif;font-weight:700;font-size:26px;line-height:1.1;color:var(--red)}
  .rally__save{margin-top:16px;font-family:"Oswald",sans-serif;font-weight:700;font-size:15px;line-height:1.2;color:var(--blue)}
  .rally__save span{color:var(--red)}
  .fight{left:292px;top:350px;width:230px}
  .fight__title{font-family:"Oswald",sans-serif;font-weight:700;font-size:21px;line-height:1.1;color:var(--red)}
  .fight__body{margin-top:4px;font-size:13px;font-weight:700;line-height:1.25;color:var(--blue)}
  .details{margin-top:12px;list-style:none}
  .details li{display:flex;align-items:flex-start;gap:8px;font-size:12px;font-weight:700;color:var(--navy);margin-bottom:9px;line-height:1.25}
  .details svg{flex:none;width:16px;height:16px}
  .lawsuit{left:288px;top:566px;width:236px;background:var(--navy);padding:9px 11px;color:var(--white)}
  .lawsuit__title{font-family:"Oswald",sans-serif;font-weight:700;font-size:14px;line-height:1.15;text-transform:uppercase}
  .lawsuit__body{margin-top:4px;font-size:8.5px;line-height:1.3;font-weight:500}
  .lawsuit__body strong{color:var(--yellow)}

  /* BACK */
  .exposed-box{left:20px;top:26px;width:225px;padding-left:12px;border-left:5px solid var(--red)}
  .exposed-box__label{font-family:"Oswald",sans-serif;font-weight:700;font-size:18px;color:var(--red)}
  .exposed-box__body{margin-top:4px;font-size:10px;font-weight:700;line-height:1.35;color:var(--blue)}
  .crowd-photo{left:258px;top:0;width:282px;height:200px;background:linear-gradient(170deg,#7fb4e6 0%,#3f5f9c 40%,#a23a3a 80%,#5a1f2a 100%)}
  .facts{left:22px;top:222px;width:496px}
  .facts__title{font-family:"Oswald",sans-serif;font-weight:700;font-size:19px;color:var(--navy);letter-spacing:.3px;margin-bottom:8px}
  .fact{margin-bottom:8px}
  .fact__head{font-family:"Montserrat",sans-serif;font-weight:800;font-size:9.5px;color:var(--red);text-transform:uppercase}
  .fact__body{font-size:8.5px;font-weight:500;line-height:1.3;color:var(--ink)}
  .web{left:24px;top:630px;font-family:"Oswald",sans-serif;font-weight:700;font-size:15px;color:var(--blue)}
  .closing{left:300px;top:620px;width:240px;height:79px;background:var(--navy);padding:12px 14px;font-family:"Oswald",sans-serif;font-weight:700;font-size:14px;line-height:1.15;color:var(--yellow);text-transform:uppercase}
  .closing span{color:var(--white);display:block;font-size:12px;margin-top:3px}
</style>
</head>
<body>

<section class="page page--front" aria-label="Flyer front">
  <div class="hero-photo abs" role="img" aria-label="Red-tinted beach photo of a lifeguard tower"></div>
  <svg class="shapes" viewBox="0 0 540 699" aria-hidden="true">
    <polygon points="276,40 540,40 540,318 276,318" fill="var(--red)"/>
    <polygon points="430,0 540,0 540,70" fill="var(--blue)"/>
    <polygon points="470,0 540,0 540,30" fill="var(--navy)"/>
    <polygon points="0,198 300,198 330,243 300,288 0,288" fill="var(--navy)" stroke="var(--red)" stroke-width="4"/>
    <polygon points="0,330 276,330 276,318 540,318 540,330 0,330" fill="var(--red)"/>
    <polygon points="0,699 0,640 120,699" fill="var(--red)"/>
    <polygon points="0,640 0,610 180,699 120,699" fill="var(--blue)"/>
    <polygon points="180,699 0,610 0,596 210,699" fill="var(--red)"/>
  </svg>
  <div class="brand abs"><span class="brand__dot"></span>EQUAL ACCESS ALLIANCE</div>
  <h1 class="headline abs">Harbor Point Exposed</h1>
  <p class="alert-banner abs">Disabled child traumatized public land abused for profit</p>

  <div class="rally abs">
    <p class="rally__invite">Join us &amp; show your support @</p>
    <p class="rally__event">SEAVIEW SHORE TOWN COUNCIL MEETING</p>
    <p class="rally__save">HELP OUR COMMUNITY SAVE HARBOR POINT PARK <span>HARBOR POINT WAS BUILT FOR FAMILIES — NOT RAVES</span></p>
  </div>

  <div class="fight abs">
    <h2 class="fight__title">Help Our Beach Community Fight Back</h2>
    <p class="fight__body">Harbor Point Park is not private. It is public property owned by the city, paid for by you.</p>
    <ul class="details">
      <li><svg viewBox="0 0 16 16"><rect x="1.5" y="3" width="13" height="11.5" rx="1.5" fill="none" stroke="var(--red)" stroke-width="1.6"/><line x1="1.5" y1="6.5" x2="14.5" y2="6.5" stroke="var(--red)" stroke-width="1.6"/><line x1="5" y1="1" x2="5" y2="4.5" stroke="var(--red)" stroke-width="1.6"/><line x1="11" y1="1" x2="11" y2="4.5" stroke="var(--red)" stroke-width="1.6"/></svg>May 14, 2025</li>
      <li><svg viewBox="0 0 16 16"><circle cx="8" cy="8" r="6.5" fill="none" stroke="var(--red)" stroke-width="1.6"/><polyline points="8,4 8,8 11,9.5" fill="none" stroke="var(--red)" stroke-width="1.6"/></svg>6:00 PM</li>
      <li><svg viewBox="0 0 16 16"><path d="M8 15s5-5.2 5-8.8A5 5 0 0 0 3 6.2C3 9.8 8 15 8 15z" fill="var(--red)"/><circle cx="8" cy="6.2" r="1.8" fill="var(--white)"/></svg>Harbor Point Park Community Room (Above The Arcade)</li>
    </ul>
  </div>

  <div class="lawsuit abs">
    <p class="lawsuit__title">Class Action Lawsuit Forming Now!</p>
    <p class="lawsuit__body">If you've been impacted by noise, denied public access, or harmed by these violations, you may be eligible for compensation. <strong>We're gathering stories and preparing legal action.</strong></p>
  </div>
</section>

<section class="page page--back" aria-label="Flyer back">
  <div class="crowd-photo abs" role="img" aria-label="Photo of a large crowd at a beachfront rave event"></div>
  <svg class="shapes" viewBox="0 0 540 699" aria-hidden="true">
    <polygon points="0,0 14,0 0,20" fill="var(--red)"/>
    <rect x="0" y="200" width="540" height="6" fill="var(--red)"/>
    <polygon points="0,699 0,660 80,699" fill="var(--red)"/>
    <polygon points="0,660 0,640 120,699 80,699" fill="var(--blue)"/>
    <polygon points="300,620 540,620 540,699 300,699" fill="var(--navy)"/>
    <polygon points="280,699 300,620 306,620 286,699" fill="var(--red)"/>
  </svg>

  <div class="exposed-box abs">
    <p class="exposed-box__label">EXPOSED:</p>
    <p class="exposed-box__body">Marco Vell, CEO of Cadence Holdings XVI LLC, the leaseholder of Harbor Point Park, has shown community outrage for profiting off public land while operating the park in ways many say violate its lease and damage our beach, our park, and our environment — all from his luxury estate in Ridgecrest Hills.</p>
  </div>

  <div class="facts abs">
    <h2 class="facts__title">WHAT THEY DON'T WANT YOU TO KNOW:</h2>
    <div class="fact"><p class="fact__head">Illegal raves – no permits.</p><p class="fact__body">Explosive concerts over 100 decibels blasting Seaview Shore with bass — multiple times per week. According to public records there are NO PERMITS and NO CITY APPROVAL.</p></div>
    <div class="fact"><p class="fact__head">The beach house isn't theirs – it's yours.</p><p class="fact__body">Harbor Point is making money with private events like "Liberty Fest" on a space built for the public from taxpayer-owned land. These takeovers appear to violate their lease and shut out families who paid for it.</p></div>
    <div class="fact"><p class="fact__head">Disabled child traumatized by rave noise</p><p class="fact__body">A child with autism and other sensory disabilities came to use the park's beach access but was overwhelmed by deafening noise and left in distress. Families say their complaints were ignored.</p></div>
    <div class="fact"><p class="fact__head">Exposed: Is Harbor Point running an unethical self-dealing scheme?</p><p class="fact__body">Harbor Point's general manager, Glen Parrish, is also CEO of a security firm hired by the park — the very company paid to "secure" its own events. Who is watching the watchers?</p></div>
    <div class="fact"><p class="fact__head">Documented illegal and suspected environmental disaster</p><p class="fact__body">Improperly stored chemicals, oil, and waste spilling into storm drains. Parking lots are blocked, flooded, and neglected. Our shoreline and wildlife are paying the price.</p></div>
    <div class="fact"><p class="fact__head">Exposed: Harbor Point Park's illegal signs mislead the public</p><p class="fact__body">They're telling the public to leave and pay for spaces that are public by law, blocking free access with signs that have no legal standing or city approval.</p></div>
    <div class="fact"><p class="fact__head">Harbor Point Park accident waiting to happen?</p><p class="fact__body">From crowded rides to overloaded walkways, safety appears ignored. The boardwalk is packed beyond capacity at night. Who will be held responsible when someone gets hurt?</p></div>
  </div>

  <p class="web abs">www.FixHarborPoint.com</p>
  <div class="closing abs">Help our community save Harbor Point Park<span>Harbor Point was built for families — not raves</span></div>
</section>

</body>
</html>
```